Restaurant needs a vertical banner for fried catfish

Our restaurant is looking for an eye-catching 78.75in. x 36in. vertical physical banner ad for our fried catfish. Photos for the fried catfish will be provided as a reference but we will also accept anything similar to the photo. We will be using the following as our receptacle: https://www.plankoria.example/banner-stand/retractable-banner-stands/
The design must incorporate the following flavor texts:
Fried Catfish
Always Fresh!
Made from Scratch
Hand-cut Fillets
The Best Catfish in Texas
Served with fries, hush puppies, and a 32oz fountain drink
Also available by the pound!
The final design should be creative, professional, and eye-catching for customers.
Updates
Colors
Designer to choose colors to be used in the design.
Requirements
Must have
- We are open to any and all design elements, albeit the 'flavor texts' should not overpower, but complement the fried catfish photo. 'Fried Catfish' can be used in lieu of a main title/logo.
Nice to have
- Transparent or textured backgrounds that can encompass any or all part of the banner such as a cutting board, shadows, abstract, etc to show depth are a plus.
- Use of vectors or objects such as ribbons or shapes to encapsulate the 'flavor texts' are also encouraged.

```html
<!DOCTYPE html>
<html lang="en">
<head>
<meta charset="utf-8">
<title>Fried Catfish Vertical Banner</title>
<link href="https://fonts.googleapis.com/css2?family=Alfa+Slab+One&family=Alegreya:wght@800&family=Source+Sans+3:wght@700&family=PT+Sans+Narrow:wght@700&display=swap" rel="stylesheet">
<style>
  :root {
    --page: #ffffff;
    --kraft: #e2c7a0;
    --kraft-light: #ead5b3;
    --kraft-dark: #c9a77b;
    --ink: #3a2a18;
    --label: #e8cfa8;
    --shadow: rgba(40, 25, 10, 0.45);
    --food-deep: #b8741f;
    --food-gold: #d39a3a;
    --food-light: #f0cf78;
  }
  * { margin: 0; padding: 0; box-sizing: border-box; }
  html, body {
    width: 1200px; height: 1000px; overflow: hidden;
    background: var(--page);
  }
  .banner {
    position: absolute; left: 403px; top: 68px;
    width: 394px; height: 864px;
    overflow: hidden;
  }
  .seafood-pattern {
    position: absolute; inset: 0;
    background:
      radial-gradient(ellipse 60% 40% at 50% 48%, var(--kraft-light) 0%, rgba(234,213,179,0) 100%),
      linear-gradient(180deg, var(--kraft-dark) 0%, var(--kraft) 20%, var(--kraft) 80%, var(--kraft-dark) 100%);
  }
  .title-plate {
    position: absolute; background: var(--label);
    box-shadow: 3px 5px 8px var(--shadow);
    border-radius: 4px;
    font-family: "Alfa Slab One", serif;
    color: var(--ink); text-align: center;
    line-height: 1;
  }
  .title-fried { left: 85px; top: 67px; width: 224px; height: 66px; font-size: 58px; padding-top: 4px; }
  .title-catfish { left: 62px; top: 127px; width: 284px; height: 64px; font-size: 56px; padding-top: 4px; }
  .tagline {
    position: absolute; top: 262px; width: 100%; text-align: center;
    font-family: "Source Sans 3", sans-serif; font-weight: 700;
    font-size: 29px; color: var(--ink);
  }
  .food-photo {
    position: absolute; left: 24px; top: 304px; width: 358px; height: 170px;
    border-radius: 50% / 50%;
    background:
      radial-gradient(ellipse closest-side at 50% 50%,
        var(--food-light) 0%, var(--food-gold) 45%, var(--food-deep) 72%,
        rgba(184,116,31,0.35) 90%, rgba(184,116,31,0) 100%);
  }
  .claim {
    position: absolute; top: 478px; width: 100%; text-align: center;
    font-family: "Alegreya", serif; font-weight: 800;
    font-size: 27px; line-height: 29px; color: var(--ink);
  }
  .info-box {
    position: absolute; left: 71px; width: 251px;
    background: var(--label);
    box-shadow: 3px 4px 7px var(--shadow);
    font-family: "PT Sans Narrow", sans-serif; font-weight: 700;
    color: var(--ink); text-align: center;
    display: flex; flex-direction: column; justify-content: center;
  }
  .info-made { top: 567px; height: 68px; }
  .info-made .small { font-size: 18px; line-height: 22px; }
  .info-made .large { font-size: 22px; line-height: 26px; }
  .info-sides { top: 652px; height: 50px; font-size: 13px; line-height: 15px; }
  .info-pound { top: 717px; height: 45px; font-size: 15px; }
</style>
</head>
<body>
  <div class="banner">
    <div class="seafood-pattern" role="img" aria-label="Kraft-paper background with engraved-style seafood sketches: fish, shrimp, octopus, shells, crab and lemon slices"></div>

    <div class="title-plate title-fried">FRIED</div>
    <div class="title-plate title-catfish">CATFISH</div>

    <p class="tagline">Always Fresh!</p>

    <div class="food-photo" role="img" aria-label="Photo of golden fried catfish fillets with french fries, hush puppies and a cup of tartar sauce"></div>

    <p class="claim">The Best Catfish<br>in Texas</p>

    <div class="info-box info-made">
      <span class="small">MADE FROM SCRATCH</span>
      <span class="large">HAND-CUT FILLETS</span>
    </div>
    <div class="info-box info-sides">
      <span>Served with fries, hush puppies,</span>
      <span>and a 32oz fountain drink</span>
    </div>
    <div class="info-box info-pound">Also available by the pound!</div>
  </div>
</body>
</html>
```